Borealis Trailworks Therapy needs Corporate Team Building Brochure

Borealis Trailworks Therapy is a new company in Vancouver Canada. We do adventure based counselling, family counselling, groups and team building events. We are looking to expand our marketing to the corporate team building world. What makes us different is that we don't just take people to play games and do adventure activities, we are able to use our training in psychology and coaching to make more of an impact. We would like to see designs that are professional and engaging, something that shows our wild adventure side. Our website is being redone, but to get a sense check out www.borealistrailworks-example.com

Target Market(s)

Vancouver downtown corporate teams.

Industry/Entity Type

Building

Font styles to use
Serif

Colors
acd037

Requirements
Must have
• some reference (visual or otherwise) to adventure activities, we do rock climbing, sea kayaking, hiking, as well as team building challenge initiatives.
• This is a flyer specifically for our team building services, it is not a general borealis trailworks therapy flyer. Use name Borealis Trailworks, not Borealis Trailworks Therapy

```html
<!DOCTYPE html>
<html lang="en">
<head>
<meta charset="utf-8">
<title>Borealis Trailworks – Corporate Team Building</title>
<link rel="stylesheet" href="https://fonts.googleapis.com/css2?family=Bree+Serif&family=Roboto+Condensed:wght@400&family=Arimo:wght@400;700&display=swap">
<style>
  :root {
    --page-bg: #ffffff;
    --panel-green: #9dca3c;
    --banner-green: #006a37;
    --frame-white: #ffffff;
    --body-ink: #1d1d1b;
    --title-ink: #3a2a1c;
    --accent-green: #00693a;
    --bullet-dark: #003a1e;
    --bullet-light: #00a04b;
    --photo-sky: #c9d6dc;
    --photo-rock: #8a9197;
    --photo-grass: #5f8a3a;
    --photo-deep: #4f7a30;
  }
  * { margin: 0; padding: 0; box-sizing: border-box; }
  html, body { width: 1200px; height: 1000px; overflow: hidden; background: var(--page-bg); }
  .spread { position: relative; width: 1200px; height: 1000px; }
  .panel { position: absolute; top: 103px; height: 794px; background: var(--panel-green); }
  .panel--left { left: 27px; width: 566px; }
  .panel--right { left: 608px; width: 565px; }

  .banner {
    position: absolute; left: 0; height: 37px;
    background: var(--banner-green); color: #fff;
    font-family: "Bree Serif", Georgia, serif; font-weight: 400; font-size: 21px;
    line-height: 37px; padding-left: 35px; white-space: nowrap;
    clip-path: polygon(0 0, 100% 0, calc(100% - 13px) 100%, 0 100%);
  }

  .body-copy {
    position: absolute;
    font-family: "Roboto Condensed", "Arial Narrow", sans-serif;
    font-size: 15px; line-height: 19.4px; color: var(--body-ink);
  }
  .body-copy p + p { margin-top: 19px; }

  .program-title {
    position: absolute;
    font-family: Arimo, Arial, sans-serif; font-weight: 400; font-size: 21px;
    color: var(--title-ink); white-space: nowrap;
  }

  .photo-frame { position: absolute; background: var(--frame-white); padding: 8px; }
  .photo-frame .photo {
    width: 100%; height: 100%;
    background: linear-gradient(180deg, var(--photo-sky) 0%, var(--photo-rock) 30%, var(--photo-grass) 55%, var(--photo-deep) 100%);
  }

  .activities-heading {
    position: absolute; font-family: Arimo, Arial, sans-serif; font-weight: 700;
    font-size: 14.5px; color: var(--accent-green);
  }
  .activity-list { position: absolute; list-style: none;
    font-family: "Roboto Condensed", "Arial Narrow", sans-serif; font-size: 15px; color: var(--body-ink); }
  .activity-list li { height: 22.5px; display: flex; align-items: center; gap: 12px; }
  .activity-list svg { width: 12px; height: 12px; flex: none; }
</style>
</head>
<body>
<main class="spread">

  <section class="panel panel--left">
    <h2 class="banner" style="top:41px; width:381px;">About Borealis Trailworks</h2>
    <div class="body-copy" style="left:34px; top:99px; width:516px;">
      <p>Borealis Trailworks brings adventure-based team building to corporate teams in downtown Vancouver. We combine outdoor challenge with real training in psychology and coaching.</p>
      <p>We don’t just take your team out to play games. Every climb, paddle and challenge is guided and debriefed by trained facilitators, so the lessons from the trail turn into better communication, trust and problem solving back at the office.</p>
      <p>Teams leave with stronger working relationships, clearer roles, more resilience under pressure and a shared story of what they achieved together.</p>
    </div>

    <h2 class="banner" style="top:385px; width:240px;">Team Climbing</h2>
    <div class="photo-frame" style="left:26px; top:446px; width:192px; height:299px;">
      <div class="photo" role="img" aria-label="Photo of a team roped up on a rock climbing wall"></div>
    </div>
    <h3 class="program-title" style="left:231px; top:450px;">Climbing for Collaboration</h3>
    <div class="body-copy" style="left:231px; top:486px; width:322px;">
      <p>A half-day or full-day climbing session that builds trust, clear communication and shared responsibility. Partners belay, coach and support each other on the wall, then our coaches lead a debrief that links each climb to how your team works day to day.</p>
      <p>Topics include: giving feedback, leading under pressure and asking for help.</p>
    </div>
  </section>

  <section class="panel panel--right">
    <h2 class="banner" style="top:41px; width:238px;">Team Paddling</h2>
    <div class="photo-frame" style="left:25px; top:97px; width:191px; height:298px;">
      <div class="photo" role="img" aria-label="Photo of a group sea kayaking together along a forested coastline"></div>
    </div>
    <h3 class="program-title" style="left:225px; top:96px;">Sea Kayak Expedition</h3>
    <div class="body-copy" style="left:225px; top:132px; width:328px;">
      <p>Move your team out of the boardroom and onto the water. Paddling in pairs and groups along the coast calls for planning, timing and steady communication, just like any big project.</p>
      <p>Our facilitators guide the day, pause for short coaching moments and finish with a debrief that helps your team name what worked and what they will take back to the office.</p>
    </div>

    <h2 class="banner" style="top:434px; width:238px;">Team Challenge</h2>
    <div class="photo-frame" style="left:25px; top:496px; width:191px; height:278px;">
      <div class="photo" role="img" aria-label="Photo of a corporate team hiking together on an alpine ridge"></div>
    </div>
    <h3 class="program-title" style="left:228px; top:495px;">Trailworks Team Day</h3>
    <div class="body-copy" style="left:228px; top:531px; width:330px;">
      <p>A custom day of hiking and challenge initiatives built around your team’s goals, led by trained counsellors and coaches who turn every activity into lasting insight.</p>
    </div>
    <h4 class="activities-heading" style="left:228px; top:639px;">Activities</h4>
    <ul class="activity-list" style="left:224px; top:662px;">
      <li><svg viewBox="0 0 12 12"><rect width="12" height="12" fill="var(--bullet-dark)"/><polygon points="4,12 8,0 12,0 8,12" fill="var(--bullet-light)"/></svg>Rock Climbing</li>
      <li><svg viewBox="0 0 12 12"><rect width="12" height="12" fill="var(--bullet-dark)"/><polygon points="4,12 8,0 12,0 8,12" fill="var(--bullet-light)"/></svg>Sea Kayaking</li>
      <li><svg viewBox="0 0 12 12"><rect width="12" height="12" fill="var(--bullet-dark)"/><polygon points="4,12 8,0 12,0 8,12" fill="var(--bullet-light)"/></svg>Hiking</li>
      <li><svg viewBox="0 0 12 12"><rect width="12" height="12" fill="var(--bullet-dark)"/><polygon points="4,12 8,0 12,0 8,12" fill="var(--bullet-light)"/></svg>Challenge Initiatives</li>
      <li><svg viewBox="0 0 12 12"><rect width="12" height="12" fill="var(--bullet-dark)"/><polygon points="4,12 8,0 12,0 8,12" fill="var(--bullet-light)"/></svg>Team Coaching Debrief</li>
    </ul>
  </section>

</main>
</body>
</html>
```